Mixed Martial Arts gym that is known for high quality athletes, students and training

We need a business card designed that is unique and stands out. Something that is not so dark and boring but looks 'energetic' to those that are given it. The customers that would receive this card would be looking to sign up for martial arts or fitness training and this card is used for corporate sponsorships and networking as well.

Marcus Pellow-Grant
0417305962 or 0409561738
Level 1, 284 Wendover Road. Westbrook Vale NSW 2893
marcus@kinetiqcombatworks.com.au
www.kinetiqcombatworks.com

```html
<!DOCTYPE html>
<html lang="en">
<head>
<meta charset="utf-8">
<title>Kinetiq Combat Works — Business Card</title>
<link href="https://fonts.googleapis.com/css2?family=Source+Sans+3:wght@400;700&display=swap" rel="stylesheet">
<style>
  :root {
    --backdrop: #d9d6d2;
    --card-light: #ffffff;
    --card-dark: #000000;
    --brand-orange: #f7941d;
    --ink: #231f20;
    --name-ink: #2b2b2b;
  }
  * { box-sizing: border-box; margin: 0; padding: 0; }
  html, body {
    width: 1200px;
    height: 1079px;
    overflow: hidden;
    background: var(--backdrop);
    font-family: "Source Sans 3", "Myriad Pro", sans-serif;
  }
  .canvas { position: relative; width: 1200px; height: 1079px; }

  .card {
    position: absolute;
    width: 856px;
    height: 490px;
  }
  .card--front {
    left: 32px; top: 28px;
    background: var(--card-light);
    border: 1px solid #8a8a8a;
  }
  .card--back {
    left: 297px; top: 558px;
    background: var(--card-dark);
  }

  .brand-name {
    color: var(--brand-orange);
    font-weight: 700;
    line-height: 1;
    text-transform: uppercase;
  }
  .card--front .brand-name {
    position: absolute;
    left: 36px; top: 70px;
    width: 330px;
    font-size: 50px;
    letter-spacing: 1px;
  }
  .card--front .brand-name span { display: block; }
  .card--front .brand-name .brand-sub {
    font-size: 24px;
    letter-spacing: 3px;
    margin-top: 8px;
  }

  .contact-list {
    position: absolute;
    left: 33px; top: 276px;
    list-style: none;
    color: var(--ink);
    font-size: 21px;
    line-height: 32px;
  }
  .contact-list li { display: flex; align-items: center; gap: 8px; }
  .contact-icon { width: 16px; height: 16px; flex: none; }

  .address {
    position: absolute;
    left: 33px; top: 434px;
    color: var(--ink);
    font-size: 21px;
  }

  .person-name {
    position: absolute;
    right: 80px; top: 262px;
    text-align: right;
    color: var(--name-ink);
    font-size: 26px;
    font-weight: 700;
    line-height: 36px;
  }

  .card--back .brand-name {
    position: absolute;
    left: 0; right: 0; top: 128px;
    text-align: center;
    font-size: 78px;
    letter-spacing: 2px;
  }
  .card--back .brand-name .brand-sub {
    display: block;
    font-size: 32px;
    letter-spacing: 4px;
    margin-top: 16px;
  }
  .back-url {
    position: absolute;
    left: 0; right: 0; top: 422px;
    text-align: center;
    color: var(--brand-orange);
    font-size: 25px;
    letter-spacing: 3px;
  }
</style>
</head>
<body>
<main class="canvas">

  <section class="card card--front">
    <h1 class="brand-name">
      <span>Kinetiq</span>
      <span class="brand-sub">Combat Works</span>
    </h1>

    <ul class="contact-list">
      <li>
        <svg class="contact-icon" viewBox="0 0 16 16" aria-hidden="true">
          <path d="M4 1.5 L6.2 4.6 L4.9 6.2 C5.8 8 7.8 10.1 9.8 11.1 L11.4 9.8 L14.5 12 L13 14.5 C7.5 14 2 8.5 1.5 3 Z" fill="var(--brand-orange)"/>
        </svg>
        0417305962
      </li>
      <li>
        <svg class="contact-icon" viewBox="0 0 16 16" aria-hidden="true">
          <path d="M4 1.5 L6.2 4.6 L4.9 6.2 C5.8 8 7.8 10.1 9.8 11.1 L11.4 9.8 L14.5 12 L13 14.5 C7.5 14 2 8.5 1.5 3 Z" fill="var(--brand-orange)"/>
        </svg>
        0409561738
      </li>
      <li>
        <svg class="contact-icon" viewBox="0 0 16 16" aria-hidden="true">
          <rect x="1" y="3" width="14" height="10" rx="1.5" fill="var(--brand-orange)"/>
          <path d="M1.5 3.8 L8 9 L14.5 3.8" fill="none" stroke="#fff" stroke-width="1.4"/>
        </svg>
        marcus@kinetiqcombatworks.com.au
      </li>
      <li>
        <svg class="contact-icon" viewBox="0 0 16 16" aria-hidden="true">
          <g fill="none" stroke="var(--brand-orange)" stroke-width="1.5">
            <circle cx="8" cy="8" r="6.5"/>
            <ellipse cx="8" cy="8" rx="2.8" ry="6.5"/>
            <line x1="1.5" y1="8" x2="14.5" y2="8"/>
          </g>
        </svg>
        www.kinetiqcombatworks.com
      </li>
    </ul>

    <p class="address">Level 1, 284 Wendover Road. Westbrook Vale NSW 2893</p>

    <p class="person-name">Marcus Pellow-<br>Grant</p>
  </section>

  <section class="card card--back">
    <h2 class="brand-name">
      Kinetiq
      <span class="brand-sub">Combat Works</span>
    </h2>
    <p class="back-url">www.kinetiqcombatworks.com</p>
  </section>

</main>
</body>
</html>
```